Business Card for Multi-Brand Sportswear Company

We are looking for a business card which represents our company and the multiple brands within it.

The company: Kelt Athletic (LTD)
The brands: Kelt, PawaLuni, VerdantFlex, Grit and Gale

Employees using these cards would be representing Kelt Athletic, rather than any of the individual brands. You will see a current design within the uploaded files, to give some inspiration. The actual text of the brands is not necessary, but the logos should be on there is some format.

Our creative minds on this are stretched, so we are looking for someone to make this their own, and show us what a good business card should look like.

We may like to get these printed with spot gloss, so keep that in mind with your designs.

www.keltathletic.co.uk

Industry/Entity Type

Business

Contact Information for Business Card

Tom Hollingsworth-Pryce
Operations Manager
(+44) 1632 960 418
Tom@keltathletic.co.uk
www.keltathletic.co.uk

Font styles to use
Sans Serif
Other font styles liked:
• Eurostile

Colors
ffffff

Requirements
Nice to have
• Dark (black) background

```html
<!DOCTYPE html>
<html lang="en">
<head>
<meta charset="utf-8">
<title>Kelt Athletic – Business Card</title>
<link rel="stylesheet" href="https://fonts.googleapis.com/css2?family=Audiowide&display=swap">
<style>
  :root {
    --page-bg: #f4f4f4;
    --card-black: #0b0b0c;
    --band-fill: #111113;
    --accent-red: #e8321f;
    --text-white: #ffffff;
    --text-soft: #d9d9d9;
    --brand-violet: #5a4fa8;
    --icon-ink: #000000;
  }
  html, body {
    margin: 0;
    width: 1050px;
    height: 1200px;
    overflow: hidden;
    background: var(--page-bg);
  }
  .card {
    position: absolute;
    left: 165px;
    top: 366px;
    width: 750px;
    height: 480px;
    background: var(--card-black);
    overflow: hidden;
    font-family: "Audiowide", sans-serif;
    color: var(--text-white);
    box-shadow: 0 6px 14px rgba(0,0,0,0.18);
  }
  .card-graphics {
    position: absolute;
    inset: 0;
  }
  .brand-row {
    position: absolute;
    top: 24px;
    right: 26px;
    display: flex;
    gap: 22px;
    align-items: center;
    font-size: 11px;
    letter-spacing: 0.5px;
  }
  .brand {
    display: flex;
    align-items: center;
    gap: 5px;
    color: var(--text-soft);
  }
  .brand .mark {
    width: 12px;
    height: 12px;
    background: var(--accent-red);
  }
  .brand .mark.violet { background: var(--brand-violet); }
  .brand .mark.round {
    width: 9px;
    height: 9px;
    border-radius: 50%;
    background: transparent;
    border: 2px solid var(--accent-red);
  }
  .company-name {
    position: absolute;
    right: 50px;
    top: 164px;
    font-size: 26px;
    letter-spacing: 1px;
    color: var(--text-white);
  }
  .person {
    position: absolute;
    right: 40px;
    top: 336px;
    text-align: right;
    text-transform: lowercase;
  }
  .person .name { font-size: 17px; letter-spacing: 1px; }
  .person .role { font-size: 12px; margin-top: 8px; letter-spacing: 1px; color: var(--text-soft); }
  .contacts {
    position: absolute;
    left: 22px;
    top: 334px;
    list-style: none;
    margin: 0;
    padding: 0;
    font-size: 15px;
  }
  .contacts li {
    display: flex;
    align-items: center;
    gap: 10px;
    height: 34px;
  }
  .contacts .icon {
    width: 18px;
    height: 18px;
    border-radius: 50%;
    background: var(--text-white);
    display: flex;
    align-items: center;
    justify-content: center;
  }
</style>
</head>
<body>
<div class="card">
  <svg class="card-graphics" width="750" height="480" viewBox="0 0 750 480" aria-hidden="true">
    <defs>
      <linearGradient id="sheen" x1="0" y1="0" x2="1" y2="0">
        <stop offset="0" stop-color="#2c2c2f" stop-opacity="0.9"/>
        <stop offset="1" stop-color="#0b0b0c" stop-opacity="0"/>
      </linearGradient>
    </defs>
    <polygon class="gloss-panel" points="0,0 40,0 405,480 0,480" fill="url(#sheen)"/>
    <line x1="40" y1="0" x2="405" y2="480" stroke="#3a3a3d" stroke-width="1"/>
    <rect class="name-band" x="200" y="108" width="570" height="116"
          fill="var(--band-fill)" stroke="var(--accent-red)" stroke-width="6"/>
  </svg>

  <div class="brand-row">
    <span class="brand"><span class="mark violet"></span>PawaLuni</span>
    <span class="brand"><span class="mark"></span>VerdantFlex</span>
    <span class="brand">Kelt</span>
    <span class="brand"><span class="mark round"></span>Grit and Gale</span>
  </div>

  <div class="company-name">Kelt Athletic</div>

  <div class="person">
    <div class="name">Tom Hollingsworth-Pryce</div>
    <div class="role">Operations Manager</div>
  </div>

  <ul class="contacts">
    <li>
      <span class="icon"><svg width="12" height="10" viewBox="0 0 12 10"><rect x="1" y="1" width="10" height="8" fill="none" stroke="var(--icon-ink)" stroke-width="1.4"/><polyline points="1,1 6,5.5 11,1" fill="none" stroke="var(--icon-ink)" stroke-width="1.4"/></svg></span>
      Tom@keltathletic.co.uk
    </li>
    <li>
      <span class="icon"><svg width="10" height="12" viewBox="0 0 10 12"><rect x="2" y="0.8" width="6" height="10.4" rx="1.2" fill="none" stroke="var(--icon-ink)" stroke-width="1.4"/><circle cx="5" cy="9" r="0.8" fill="var(--icon-ink)"/></svg></span>
      (+44) 1632 960 418
    </li>
    <li>
      <span class="icon"><svg width="12" height="12" viewBox="0 0 12 12"><circle cx="6" cy="6" r="5" fill="none" stroke="var(--icon-ink)" stroke-width="1.2"/><ellipse cx="6" cy="6" rx="2.2" ry="5" fill="none" stroke="var(--icon-ink)" stroke-width="1"/><line x1="1" y1="6" x2="11" y2="6" stroke="var(--icon-ink)" stroke-width="1"/></svg></span>
      www.keltathletic.co.uk
    </li>
  </ul>
</div>
</body>
</html>
```